Equity, Effectiveness and Efficiency in charitable food relief sector

I am undertaking my PhD in food policy in the charitable food relief sector, specifically investigating the factors (supply, demand and capacity) that affect the introduction of nutrition policy and in turn, affect the sector's ability to achieve equity, effectiveness and efficiency.

I need a graphic device that incorporates this central idea of Equity, Effectiveness and Efficiency, and how the factors of supply, demand and capacity interact. There are sub-factors within supply (1-6), demand (7-10) and capacity (11 - 15). All these details are shown in the attached figure (Basic figure_Eq Effec Effic and factors.jpg)

This figure (Basic figure_Eq Effec Effic and factors.jpg) contains all the information I need in a graphic but I need something that is more visually appealing, and that can link the ideas in a format other than a table. The final graphic will outline how the food relief sector balances the core objectives of equity, effectiveness and efficiency with the factors (and sub-factors) of supply, demand and capacity.

```html
<!DOCTYPE html>
<html lang="en">
<head>
<meta charset="utf-8">
<title>Equity, Effectiveness, Efficiency — Factors of Nutrition Policy</title>
<link rel="stylesheet" href="https://fonts.googleapis.com/css2?family=Source+Sans+3:wght@400;500&display=swap">
<style>
  :root {
    --orange: #e36703;
    --slate: #59595b;
    --navy: #1a1c28;
    --white: #ffffff;
  }
  html, body {
    margin: 0;
    padding: 0;
    width: 1144px;
    height: 1200px;
    overflow: hidden;
    background: var(--white);
  }
  .diagram {
    display: block;
    width: 1144px;
    height: 1200px;
    font-family: "Source Sans 3", "Myriad Pro", sans-serif;
  }
  .core { fill: var(--orange); }
  .core-label { fill: var(--white); font-size: 64px; font-weight: 400; text-anchor: middle; }
  .connector { fill: var(--slate); }
  .factors-label { fill: var(--white); font-size: 37px; letter-spacing: 2.6px; text-anchor: middle; }
  .pill { fill: var(--navy); }
  .pill-title { fill: var(--white); font-size: 76px; font-weight: 400; }
  .pill-mark { fill: var(--white); }
  .list-box { fill: var(--slate); }
  .item { fill: var(--white); font-size: 25px; letter-spacing: 1.7px; }
  .bullet { fill: var(--white); }
  .icon-arrow { fill: none; stroke: var(--navy); stroke-width: 4; stroke-linecap: square; }
</style>
</head>
<body>
<svg class="diagram" viewBox="0 0 1875 1967" xmlns="http://www.w3.org/2000/svg" role="img" aria-label="Equity, effectiveness and efficiency shaped by supply, demand and capacity factors">

  <!-- Core objectives -->
  <circle class="core" cx="935" cy="475" r="247"/>
  <text class="core-label" x="930" y="406">EQUITY</text>
  <text class="core-label" x="930" y="492">EFFECTIVENESS</text>
  <text class="core-label" x="935" y="577">EFFICIENCY</text>

  <!-- Connectors -->
  <path class="connector" d="M883 741 Q935 749 987 741 L987 803 L883 803 Z"/>
  <path class="connector" d="M287 1031 L287 868 Q287 823 332 823 L1537 823 Q1582 823 1582 868 L1582 1031 L1636 1031 L1530 1137 L1425 1031 L1478 1031 L1478 916 L391 916 L391 1031 L445 1031 L339 1137 L233 1031 Z"/>
  <path class="connector" d="M885 935 L985 935 L985 1006 L1038 1006 L935 1108 L832 1006 L885 1006 Z"/>
  <text class="factors-label" x="947" y="885">FACTORS AFFECTING THE INTRODUCTION OF NUTRITION POLICY</text>

  <!-- Supply -->
  <g class="factor factor-supply">
    <rect class="pill" x="95" y="1152" width="480" height="107" rx="53.5"/>
    <text class="pill-title" x="168" y="1233">SUPPLY</text>
    <polygon class="pill-mark" points="438,1168 458,1168 498,1206 458,1244 438,1244 478,1206"/>
    <path class="list-box" d="M121 1273 Q335 1282 548 1273 L548 1543 Q548 1578 513 1578 L156 1578 Q121 1578 121 1543 Z"/>
    <g>
      <circle class="bullet" cx="145" cy="1314" r="6.5"/><text class="item" x="166" y="1322">UNCERTAIN MATERIAL SUPPLY</text>
      <circle class="bullet" cx="145" cy="1358" r="6.5"/><text class="item" x="166" y="1366">UNCERTAIN MONETARY SUPPLY</text>
      <circle class="bullet" cx="145" cy="1402" r="6.5"/><text class="item" x="166" y="1410">LIMITED FOOD SUPPLY</text>
      <circle class="bullet" cx="145" cy="1447" r="6.5"/><text class="item" x="166" y="1455">PERISHABILITY</text>
      <circle class="bullet" cx="145" cy="1490" r="6.5"/><text class="item" x="166" y="1498">DONOR CONSTRAINTS</text>
      <circle class="bullet" cx="145" cy="1535" r="6.5"/><text class="item" x="166" y="1543">DONOR RELATIONSHIPS</text>
    </g>
  </g>

  <!-- Demand -->
  <g class="factor factor-demand">
    <rect class="pill" x="684" y="1152" width="502" height="107" rx="53.5"/>
    <text class="pill-title" x="740" y="1233">DEMAND</text>
    <polygon class="pill-mark" points="1125,1168 1105,1168 1065,1206 1105,1244 1125,1244 1085,1206"/>
    <path class="list-box" d="M722 1277 Q935 1284 1149 1277 L1149 1441 Q1149 1476 1114 1476 L757 1476 Q722 1476 722 1441 Z"/>
    <g>
      <circle class="bullet" cx="763" cy="1315" r="6.5"/><text class="item" x="783" y="1323">UNCERTAIN DEMAND</text>
      <circle class="bullet" cx="763" cy="1359" r="6.5"/><text class="item" x="783" y="1367">LIMITED DEMAND VISIBILITY</text>
      <circle class="bullet" cx="763" cy="1403" r="6.5"/><text class="item" x="783" y="1411">CLIENT CHOICE</text>
      <circle class="bullet" cx="763" cy="1447" r="6.5"/><text class="item" x="783" y="1455">FOOD WASTAGE</text>
    </g>
  </g>

  <!-- Capacity -->
  <g class="factor factor-capacity">
    <rect class="pill" x="1266" y="1152" width="515" height="107" rx="53.5"/>
    <text class="pill-title" x="1311" y="1233">CAPACITY</text>
    <g class="expand-icon">
      <circle class="pill-mark" cx="1695" cy="1205" r="46"/>
      <path class="icon-arrow" d="M1669 1179 L1691 1179 M1669 1179 L1669 1201 M1669 1179 L1687 1197"/>
      <path class="icon-arrow" d="M1721 1179 L1699 1179 M1721 1179 L1721 1201 M1721 1179 L1703 1197"/>
      <path class="icon-arrow" d="M1669 1231 L1691 1231 M1669 1231 L1669 1209 M1669 1231 L1687 1213"/>
      <path class="icon-arrow" d="M1721 1231 L1699 1231 M1721 1231 L1721 1209 M1721 1231 L1703 1213"/>
    </g>
    <path class="list-box" d="M1310 1277 Q1523 1284 1737 1277 L1737 1705 Q1737 1740 1702 1740 L1345 1740 Q1310 1740 1310 1705 Z"/>
    <g>
      <circle class="bullet" cx="1339" cy="1314" r="6.5"/><text class="item" x="1359" y="1322">STORAGE</text>
      <text class="item" x="1383" y="1359">A) COLD</text>
      <text class="item" x="1383" y="1388">B) WAREHOUSE</text>
      <circle class="bullet" cx="1339" cy="1432" r="6.5"/><text class="item" x="1359" y="1440">TRANSPORTATION</text>
      <circle class="bullet" cx="1339" cy="1476" r="6.5"/><text class="item" x="1359" y="1484">WORKFORCE</text>
      <text class="item" x="1383" y="1523">A) VOLUNTEERS</text>
      <text class="item" x="1383" y="1551">B) EXPERTISE AND TRAINING</text>
      <text class="item" x="1383" y="1577">C) ATTITUDES AND BELIEFS</text>
      <text class="item" x="1383" y="1605">D) COLLABORATION</text>
      <text class="item" x="1383" y="1634">E) EXECUTIVE SUPPORT</text>
      <circle class="bullet" cx="1339" cy="1666" r="6.5"/><text class="item" x="1359" y="1674">EXTERNAL STAKEHOLDERS</text>
      <circle class="bullet" cx="1339" cy="1709" r="6.5"/><text class="item" x="1359" y="1717">BUDGET</text>
    </g>
  </g>
</svg>
</body>
</html>
```